Business card design needed

It's a new business in town.Something so the name stands out.I need a logo for the B.R.K
I may all so use the design as a sign on a building

Contact Information for Business Card

B.R.K
Brackenvale Auto Detailing
42 Tillbury Crs
Brackenvale Vic 3819
Ph:(03)58264027
Mob:0417392658

```html
<!DOCTYPE html>
<html lang="en">
<head>
<meta charset="utf-8">
<title>Brackenvale Auto Detailing – Business Card</title>
<link rel="stylesheet" href="https://fonts.googleapis.com/css2?family=Tinos&family=Kalam:wght@400&display=swap">
<style>
  :root {
    --sea-deep: #2478bd;
    --sea-mid: #33a3d3;
    --sea-teal: #44a9a8;
    --ink: #0d1418;
    --paper: #f4f6f7;
  }
  html, body {
    margin: 0;
    padding: 0;
    overflow: hidden;
    background: #ffffff;
  }
  .card {
    position: relative;
    width: 1200px;
    height: 741px;
    overflow: hidden;
    font-family: "Tinos", "Times New Roman", serif;
  }
  .card-backdrop {
    position: absolute;
    inset: 0;
    background:
      radial-gradient(circle 330px at 830px 400px, rgba(120, 210, 230, 0.28), transparent 75%),
      radial-gradient(ellipse 260px 340px at 90px 400px, rgba(80, 180, 205, 0.35), transparent 70%),
      linear-gradient(125deg, var(--sea-deep) 0%, var(--sea-mid) 45%, #3aa6c9 70%, var(--sea-teal) 100%);
  }
  .brand-name {
    position: absolute;
    left: 84px;
    top: 298px;
    margin: 0;
    font-family: "Tinos", "Times New Roman", serif;
    font-weight: 400;
    font-size: 128px;
    line-height: 1;
    letter-spacing: -4px;
    color: var(--paper);
  }
  .business-details {
    position: absolute;
    left: 432px;
    top: 288px;
    margin: 0;
    font-size: 46px;
    line-height: 58px;
    letter-spacing: 1px;
    white-space: nowrap;
  }
  .business-name {
    display: block;
    color: var(--paper);
  }
  .business-address {
    display: block;
    color: var(--ink);
  }
  .contact-line {
    position: absolute;
    left: 99px;
    height: 100px;
    display: flex;
    align-items: center;
    gap: 28px;
  }
  .contact-line.mobile { top: 526px; }
  .contact-line.landline { top: 626px; }
  .contact-icon {
    width: 100px;
    height: 100px;
    flex: none;
  }
  .contact-number {
    font-family: "Kalam", "Comic Sans MS", cursive;
    font-size: 72px;
    line-height: 1;
    letter-spacing: 10px;
    color: var(--ink);
    padding-top: 12px;
  }
</style>
</head>
<body>
<main class="card">
  <div class="card-backdrop" role="img" aria-label="Textured blue and teal painted background with faint splashes and diagonal streaks"></div>

  <h1 class="brand-name">B.R.K</h1>

  <p class="business-details">
    <span class="business-name">Brackenvale Auto Detailing</span>
    <span class="business-address">42 Tillbury Crs Brackenvale Vic 3819</span>
  </p>

  <div class="contact-line mobile">
    <svg class="contact-icon" viewBox="0 0 100 100" aria-hidden="true">
      <circle cx="50" cy="50" r="45" fill="none" stroke="#0d1418" stroke-width="6"/>
      <rect x="37" y="28" width="26" height="52" rx="5" fill="#0d1418"/>
      <rect x="58" y="14" width="4" height="16" fill="#0d1418"/>
      <rect x="41" y="33" width="18" height="14" fill="#3aa6c9"/>
      <g fill="#3aa6c9">
        <rect x="41" y="52" width="4" height="4"/><rect x="48" y="52" width="4" height="4"/><rect x="55" y="52" width="4" height="4"/>
        <rect x="41" y="59" width="4" height="4"/><rect x="48" y="59" width="4" height="4"/><rect x="55" y="59" width="4" height="4"/>
        <rect x="41" y="66" width="4" height="4"/><rect x="48" y="66" width="4" height="4"/><rect x="55" y="66" width="4" height="4"/>
        <rect x="41" y="73" width="4" height="3"/><rect x="48" y="73" width="4" height="3"/><rect x="55" y="73" width="4" height="3"/>
      </g>
    </svg>
    <span class="contact-number">0417392658</span>
  </div>

  <div class="contact-line landline">
    <svg class="contact-icon" viewBox="0 0 100 100" aria-hidden="true">
      <circle cx="50" cy="50" r="45" fill="none" stroke="#0d1418" stroke-width="6"/>
      <path d="M20 40 Q50 22 80 40 L80 46 L68 46 L66 38 Q50 33 34 38 L32 46 L20 46 Z" fill="#0d1418"/>
      <path d="M34 48 L66 48 L76 74 L24 74 Z" fill="#0d1418"/>
      <g fill="#3aa6c9">
        <rect x="40" y="54" width="5" height="4"/><rect x="48" y="54" width="5" height="4"/><rect x="56" y="54" width="5" height="4"/>
        <rect x="38" y="61" width="5" height="4"/><rect x="48" y="61" width="5" height="4"/><rect x="58" y="61" width="5" height="4"/>
        <rect x="36" y="67" width="5" height="4"/><rect x="48" y="67" width="5" height="4"/><rect x="60" y="67" width="5" height="4"/>
      </g>
    </svg>
    <span class="contact-number">(03)58264027</span>
  </div>
</main>
</body>
</html>
```